Novu Staffing Tri Fold Brochure

My company is a recruiting/staffing firm. I need a design that is going to be professional, bright, young, hip and fun. Pictures are key! We want people working in an office, packaging, food production and/or light industrial environment. Must embrace DIVERSITY. Please use the 4 primary colors from the Novu Logo to accent the piece, but not too busy. I am including the content that I would like to be included in the trifold as well as a sample of a trifold I have used in the past in addition to a couple of logos. My website is www.NovuStaffing.example for look and feel.

Target Market(s)

Logistics, Distribution and Manufacturing companies

Industry/Entity Type

Staffing

Requirements
Must have
• Clean, colorful, eye catching, great pictures and graphics. Photo's of diverse people working, in a office, or production setting.
Nice to have
• Must be professional
Should not have
• Not too busy.

```html
<!DOCTYPE html>
<html lang="en">
<head>
<meta charset="utf-8">
<title>Novu Staffing – Tri-Fold Brochure</title>
<link rel="stylesheet" href="https://fonts.googleapis.com/css2?family=Montserrat:wght@400;500;600;700;800&family=Open+Sans:ital,wght@0,400;0,700;1,700&family=Oswald:wght@300;500;600&display=swap">
<style>
:root{
  --red:#e8352a;
  --yellow:#e9c221;
  --green:#1f7a3a;
  --navy:#27286b;
  --ink:#222;
  --paper:#f4f4f6;
  --panel-grey:#ececef;
  --stage:#6a6a6a;
}
*{box-sizing:border-box;margin:0;padding:0}
html,body{width:851px;height:1200px;overflow:hidden}
body{background:var(--stage);font-family:"Montserrat",sans-serif;color:var(--ink);position:relative}
.spread{position:absolute;left:20px;width:811px;height:573px;background:var(--paper);overflow:hidden}
.spread--outside{top:18px}
.spread--inside{top:609px}
.abs{position:absolute}
.shapes{position:absolute;left:0;top:0;width:811px;height:573px}
.photo{position:absolute}
.photo--round{border-radius:50%;border:3px solid var(--yellow)}

/* outside: panel 1 */
.photo-technician{left:0;top:0;width:270px;height:290px;background:linear-gradient(135deg,#5a3d8a 0%,#8a6fb0 35%,#c9b59a 65%,#4b5670 100%);clip-path:polygon(0 0,100% 0,100% 72%,72% 96%,0 96%)}
.photo-crew{left:15px;top:272px;width:160px;height:160px;background:radial-gradient(circle at 50% 45%,#c7b07a,#6b6d73 55%,#2f3d67)}
.quote{position:absolute;right:578px;text-align:right;color:var(--navy)}
.quote-mark{font-weight:800;font-size:34px;line-height:1;top:396px;right:578px}
.quote-yes{top:415px;font-weight:700;font-size:34px;line-height:1}
.quote-line{font-size:14px;font-weight:500;white-space:nowrap}
.quote-line b{font-weight:700}
.quote-yeah{position:absolute;left:52px;top:484px;font-size:33px;font-weight:700;color:var(--navy);line-height:1}
.quote-have{position:absolute;right:578px;top:487px;text-align:left;font-size:13px;line-height:14px;color:var(--navy);font-weight:500}
.quote-have b{font-weight:700}

/* outside: panel 2 */
.photo-meeting{left:270px;top:0;width:271px;height:340px;background:linear-gradient(160deg,#dfe4e6 0%,#aeb6ba 40%,#4c4a4d 75%,#2c2b2e 100%)}
.brand{position:absolute;color:var(--navy);font-weight:700;line-height:1;text-align:center}
.brand small{display:block;font-weight:700;letter-spacing:1px}
.brand--mid{left:300px;top:212px;width:110px;font-size:30px}
.brand--mid small{font-size:9px;margin-top:2px}
.locations-title{position:absolute;left:310px;top:280px;font-size:15.5px;font-weight:700;color:var(--red);display:flex;align-items:center;gap:7px}
.locations-rule{position:absolute;left:310px;top:302px;width:146px;height:1px;background:#222}
.loc-list{position:absolute;left:310px;top:319px;width:150px;font-size:8.8px;line-height:11.8px}
.loc-state{color:var(--green);font-weight:700;margin-top:10px}
.loc-state:first-child{margin-top:0}
.loc-row{display:flex}
.loc-row span:first-child{width:72px}
.site-pill{position:absolute;left:296px;top:522px;width:220px;height:24px;border-radius:12px;background:var(--navy);color:#fff;font-size:11px;font-weight:600;letter-spacing:1.2px;display:flex;align-items:center;justify-content:center;gap:6px}

/* outside: panel 3 (cover) */
.photo-team{left:541px;top:143px;width:270px;height:260px;background:linear-gradient(120deg,#8d8e92 0%,#c9b29c 30%,#6f7681 55%,#c9c3bb 80%,#3e3f45 100%)}
.brand--cover{left:596px;top:40px;width:170px;font-size:58px;text-align:left}
.brand--cover small{font-size:18px;text-align:right;margin-top:2px;font-weight:700}
.cover-headline{position:absolute;left:573px;top:406px;color:#fff;font-weight:800;font-size:19.5px;line-height:23.5px;letter-spacing:.3px}
.cover-rule{position:absolute;left:573px;top:511px;width:197px;height:1.5px;background:#fff}
.cover-site{position:absolute;left:573px;top:528px;color:#fff;font-size:11.5px;font-weight:600;letter-spacing:1.6px;display:flex;align-items:center;gap:6px}

/* inside: panel 1 */
.label-bar{position:absolute;left:24px;width:220px;height:24px;background:var(--red);color:#fff;font-weight:700;font-size:12.5px;letter-spacing:.3px;display:flex;align-items:center;padding-left:14px}
.definition{position:absolute;left:24px;top:55px;width:220px;color:var(--navy);font-size:9px;font-weight:700}
.definition em{display:block;margin-top:5px;font-family:"Open Sans",sans-serif;font-style:italic;color:#222;font-size:8px;line-height:11.5px}
.body-copy{font-family:"Open Sans",sans-serif;font-size:7.4px;line-height:11.1px;text-align:justify;color:#333}
.philosophy{position:absolute;left:24px;top:132px;width:220px}
.difference{position:absolute;left:24px;top:218px;list-style:none;color:var(--navy);font-size:8.9px;font-weight:500;line-height:14.3px}
.tick-list li{display:flex;align-items:center;gap:5px}
.tick{width:8px;height:8px;flex:none}
.about{position:absolute;left:24px;top:294px;width:220px}
.photo-workers{left:0;top:385px;width:270px;height:188px;background:linear-gradient(180deg,#d9d9dd 0%,#a77a5c 40%,#1f2a5a 70%,#1b2250 100%);clip-path:polygon(0 30%,18% 30%,36% 0,54% 0,72% 22%,100% 22%,100% 100%,0 100%)}

/* inside: panels 2–3 */
.photo-collab{left:330px;top:0;width:481px;height:300px;background:linear-gradient(135deg,#c9b48a 0%,#6d7078 30%,#d9d6d2 55%,#3a3636 78%,#8b5b48 100%);clip-path:polygon(0 0,100% 0,100% 31%,59% 98%,45% 98%,0 28%)}
.photo-interview{left:286px;top:79px;width:114px;height:114px;background:radial-gradient(circle at 50% 40%,#e7dfd4,#9aa0a8 60%,#4f5460)}
.solutions{position:absolute;left:297px;top:207px;font-family:"Oswald",sans-serif;line-height:1}
.solutions-top{font-size:31px;font-weight:300;color:var(--navy);letter-spacing:4.2px}
.solutions-bottom{font-size:32px;font-weight:600;color:var(--red);letter-spacing:2.4px;margin-top:3px}
.cta-badge{position:absolute;left:652px;top:160px;width:130px;height:130px;border-radius:50%;background:var(--navy);border:3px solid var(--yellow);font-family:"Oswald",sans-serif;font-weight:500;font-size:16.5px;line-height:18px;text-align:center;color:#fff;display:flex;flex-direction:column;justify-content:center}
.cta-badge span{color:var(--yellow)}
.apart-banner{position:absolute;left:298px;top:301px;width:488px;height:37px;background:var(--red);border-radius:3px;color:#fff;font-weight:700;font-size:9.9px;line-height:13px;text-align:center;display:flex;align-items:center;justify-content:center}
.service{position:absolute;width:222px}
.service h3{font-size:10.6px;font-weight:700;color:var(--navy);padding-bottom:2px;border-bottom:1px solid var(--green);margin-bottom:5px}
.service .body-copy{font-size:7.1px;line-height:10.4px}
.service--staffing{left:298px;top:351px}
.service--c2h{left:298px;top:422px}
.service--direct{left:298px;top:493px}
.service--managed{left:564px;top:351px}
.industries-bar{position:absolute;left:564px;top:431px;width:222px;height:17px;background:var(--red);color:#fff;font-size:10px;font-weight:700;display:flex;align-items:center;justify-content:center}
.industries{position:absolute;top:455px;list-style:none;color:var(--navy);font-size:8.4px;font-weight:500;line-height:12.8px}
.industries--a{left:564px}
.industries--b{left:690px}
</style>
</head>
<body>

<!-- Outside spread: back panel, inside flap, front cover -->
<section class="spread spread--outside">
  <div class="photo photo-technician" role="img" aria-label="Photo: young technician assembling electronic parts at a workbench"></div>
  <div class="photo photo-meeting" role="img" aria-label="Photo: diverse team meeting around a table in a bright office"></div>
  <div class="photo photo-team" role="img" aria-label="Photo: smiling diverse business professionals seated in a row"></div>

  <svg class="shapes" viewBox="0 0 811 573" aria-hidden="true">
    <path d="M0 0 H40 Q44 0 40 6 L0 68 Z" fill="var(--yellow)"/>
    <path d="M0 290 L190 290 L270 205 L270 573 L0 573 Z" fill="var(--paper)"/>
    <path d="M270 215 L338 168 Q352 158 366 170 L541 334 L541 573 L270 573 Z" fill="var(--paper)"/>
    <rect x="541" y="0" width="270" height="143" fill="#fafafa"/>
    <path d="M730 0 H811 V22 L786 44 Q780 48 772 42 Z" fill="var(--green)"/>
    <circle cx="178" cy="293" r="37" fill="#ee8a70" opacity=".85"/>
    <circle cx="234" cy="263" r="19" fill="var(--yellow)" opacity=".75"/>
    <path d="M400 573 L541 437 L541 573 Z" fill="var(--red)"/>
    <path d="M541 437 L642 348 Q656 336 670 348 L811 470 L811 573 L541 573 Z" fill="var(--red)"/>
    <path d="M736 377 L762 355 Q772 348 782 356 L811 382 L811 466 Z" fill="var(--yellow)"/>
  </svg>

  <!-- back panel quote -->
  <div class="photo photo--round photo-crew" role="img" aria-label="Photo: industrial workers in hard hats and safety vests"></div>
  <div class="quote quote-mark">“</div>
  <div class="quote quote-yes">YES</div>
  <div class="quote quote-line" style="top:452px">the <b>CANDIDATE</b></div>
  <div class="quote quote-line" style="top:470px">meets the <b>requirements,</b></div>
  <div class="quote-yeah">YEAH</div>
  <div class="quote-have">they <b>HAVE</b><br>the skills,</div>
  <div class="quote quote-line" style="top:524px;font-size:16px">but do they <b>NOVU?</b> <b style="font-size:26px;line-height:0;vertical-align:-6px">”</b></div>

  <!-- locations flap -->
  <div class="brand brand--mid">Novu<small>staffing</small></div>
  <div class="locations-title">
    <svg width="10" height="14" viewBox="0 0 10 14" aria-hidden="true"><circle cx="5" cy="4.5" r="3.3" fill="none" stroke="var(--green)" stroke-width="1.5"/><path d="M5 8 V12 M1.5 13 H8.5" stroke="var(--green)" stroke-width="1.5"/></svg>
    Locations
  </div>
  <div class="locations-rule"></div>
  <div class="loc-list">
    <div class="loc-state">Georgia</div>
    <div class="loc-row"><span>Cartersville -</span><span>555-201-4410</span></div>
    <div class="loc-row"><span>Marietta -</span><span>555-201-4422</span></div>
    <div class="loc-row"><span>Savannah -</span><span>555-201-4435</span></div>
    <div class="loc-row"><span>Union City -</span><span>555-201-4447</span></div>
    <div class="loc-state">Indiana</div>
    <div class="loc-row"><span>Plainfield -</span><span>555-301-7720</span></div>
    <div class="loc-state">Pennsylvania</div>
    <div class="loc-row"><span>Harrisburg -</span><span>555-401-3380</span></div>
    <div class="loc-row"><span>Bethlehem -</span><span>555-401-3395</span></div>
    <div class="loc-state">Texas</div>
    <div class="loc-row"><span>Arlington -</span><span>555-501-6610</span></div>
  </div>
  <div class="site-pill">
    <svg width="10" height="10" viewBox="0 0 10 10" aria-hidden="true"><circle cx="5" cy="5" r="4.2" fill="none" stroke="#fff"/><path d="M0.8 5 H9.2 M5 0.8 C2.5 3 2.5 7 5 9.2 M5 0.8 C7.5 3 7.5 7 5 9.2" fill="none" stroke="#fff" stroke-width=".8"/></svg>
    www.NovuStaffing.example
  </div>

  <!-- front cover -->
  <div class="brand brand--cover">Novu<small>staffing</small></div>
  <div class="cover-headline">CONNECTING<br>GREAT PEOPLE<br>WITH<br>GREAT COMPANIES</div>
  <div class="cover-rule"></div>
  <div class="cover-site">
    <svg width="10" height="10" viewBox="0 0 10 10" aria-hidden="true"><circle cx="5" cy="5" r="4.2" fill="none" stroke="#fff"/><path d="M0.8 5 H9.2 M5 0.8 C2.5 3 2.5 7 5 9.2 M5 0.8 C7.5 3 7.5 7 5 9.2" fill="none" stroke="#fff" stroke-width=".8"/></svg>
    www.NovuStaffing.example
  </div>
</section>

<!-- Inside spread -->
<section class="spread spread--inside">
  <svg class="shapes" viewBox="0 0 811 573" aria-hidden="true">
    <rect x="270" y="0" width="271" height="573" fill="var(--panel-grey)"/>
    <rect x="541" y="0" width="270" height="573" fill="#f1f1f3"/>
    <path d="M740 158 L811 93 L811 307 Z" fill="var(--green)"/>
  </svg>

  <div class="photo photo-collab" role="img" aria-label="Photo: diverse colleagues leaning over a desk reviewing plans together"></div>
  <div class="photo photo-workers" role="img" aria-label="Photo: smiling diverse production team in navy caps and shirts"></div>

  <!-- panel 1 -->
  <div class="label-bar" style="top:25px">DEFINITION OF NOVU - verb</div>
  <div class="definition">To be in harmony or accord; To fit; Agree:
    <em>“Yes the candidate meets the requirements, yeah they have the skills, but do they Novu?”</em>
  </div>
  <div class="label-bar" style="top:101px">NOVU'S PHILOSOPHY:</div>
  <p class="body-copy philosophy">To conduct business with the highest degree of morals, values and integrity. To do the right thing each and every day and treat our business partners, and employees honestly, fairly and with respect.</p>
  <div class="label-bar" style="top:188px">THE NOVU DIFFERENCE:</div>
  <ul class="difference tick-list">
    <li><svg class="tick" viewBox="0 0 10 10"><circle cx="5" cy="5" r="4.3" fill="none" stroke="var(--green)"/><path d="M2.8 5.2 L4.4 6.7 L7.3 3.6" fill="none" stroke="var(--green)"/></svg>SCREENING AND SELECTION PROCESS</li>
    <li><svg class="tick" viewBox="0 0 10 10"><circle cx="5" cy="5" r="4.3" fill="none" stroke="var(--green)"/><path d="M2.8 5.2 L4.4 6.7 L7.3 3.6" fill="none" stroke="var(--green)"/></svg>SPEED OF DELIVERY</li>
    <li><svg class="tick" viewBox="0 0 10 10"><circle cx="5" cy="5" r="4.3" fill="none" stroke="var(--green)"/><path d="M2.8 5.2 L4.4 6.7 L7.3 3.6" fill="none" stroke="var(--green)"/></svg>PRETRAINING PROGRAMS</li>
    <li><svg class="tick" viewBox="0 0 10 10"><circle cx="5" cy="5" r="4.3" fill="none" stroke="var(--green)"/><path d="M2.8 5.2 L4.4 6.7 L7.3 3.6" fill="none" stroke="var(--green)"/></svg>CUSTOM ORIENTATIONS</li>
    <li><svg class="tick" viewBox="0 0 10 10"><circle cx="5" cy="5" r="4.3" fill="none" stroke="var(--green)"/><path d="M2.8 5.2 L4.4 6.7 L7.3 3.6" fill="none" stroke="var(--green)"/></svg>CUSTOMER SERVICE</li>
  </ul>
  <p class="body-copy about"><b>Novu</b> Staffing is a full service staffing and recruiting firm dedicated to helping com-panies attract and retain the best talent available for their specific hiring needs. We source candidates that have the skills, experience and personality to seamlessly fit into the culture of your company. We listen to your needs and develop custom solutions that bring tangible results to our client's business.</p>

  <!-- panels 2–3 -->
  <div class="photo photo--round photo-interview" role="img" aria-label="Photo: job candidate interviewed by a panel"></div>
  <div class="solutions">
    <div class="solutions-top">SOLUTIONS</div>
    <div class="solutions-bottom">THAT MATTER</div>
  </div>
  <div class="cta-badge">Take the<br>first step toward<br><span>a better<br>opportunity</span></div>
  <div class="apart-banner">WHAT SETS NOVU APART IS OUR INDUSTRY KNOWLEDGE AND ABILITY TO<br>PROVIDE TAILORED SOLUTIONS TO EACH MARKET WE SERVICE.</div>

  <div class="service service--staffing">
    <h3>CONTRACT STAFFING SOLUTIONS</h3>
    <p class="body-copy">Enables you to fill both short-term and long-term needs with quality associates to support projects or seasonal needs. Gives you flexibility to retain talent while reducing employee related costs.</p>
  </div>
  <div class="service service--c2h">
    <h3>CONTRACT TO HIRE SOLUTIONS</h3>
    <p class="body-copy">Gives you the opportunity to observe the associ-ates and determine if they are the right fit for your team and culture. After the contract period is complete, you can hire the associate on a permanent basis.</p>
  </div>
  <div class="service service--direct">
    <h3>DIRECT HIRE SOLUTIONS</h3>
    <p class="body-copy"><b>Novu</b> will assume all responsibility to recruit and screen candidates so you can focus on your business. Leave it to our recruiters with access to a wide range of recruiting sources to find the perfect fit for your organization.</p>
  </div>
  <div class="service service--managed">
    <h3>MANAGED SERVICES</h3>
    <p class="body-copy">In addition to hiring the highest quality candi-dates, <b>Novu</b> offers complete workforce manage-ment or onsite programs. Our onsite perfor-mance manager is responsible for hiring, manag-ing, training, driving production and handling all associate issues.</p>
  </div>

  <div class="industries-bar">INDUSTRIES WE SERVE:</div>
  <ul class="industries industries--a tick-list">
    <li><svg class="tick" viewBox="0 0 10 10"><circle cx="5" cy="5" r="4.3" fill="none" stroke="var(--green)"/><path d="M2.8 5.2 L4.4 6.7 L7.3 3.6" fill="none" stroke="var(--green)"/></svg>ADMINISTRATIVE</li>
    <li><svg class="tick" viewBox="0 0 10 10"><circle cx="5" cy="5" r="4.3" fill="none" stroke="var(--green)"/><path d="M2.8 5.2 L4.4 6.7 L7.3 3.6" fill="none" stroke="var(--green)"/></svg>ACCOUNTING</li>
    <li><svg class="tick" viewBox="0 0 10 10"><circle cx="5" cy="5" r="4.3" fill="none" stroke="var(--green)"/><path d="M2.8 5.2 L4.4 6.7 L7.3 3.6" fill="none" stroke="var(--green)"/></svg>CALL CENTER</li>
    <li><svg class="tick" viewBox="0 0 10 10"><circle cx="5" cy="5" r="4.3" fill="none" stroke="var(--green)"/><path d="M2.8 5.2 L4.4 6.7 L7.3 3.6" fill="none" stroke="var(--green)"/></svg>DISTRIBUTION</li>
    <li><svg class="tick" viewBox="0 0 10 10"><circle cx="5" cy="5" r="4.3" fill="none" stroke="var(--green)"/><path d="M2.8 5.2 L4.4 6.7 L7.3 3.6" fill="none" stroke="var(--green)"/></svg>FOOD PRODUCTION</li>
    <li><svg class="tick" viewBox="0 0 10 10"><circle cx="5" cy="5" r="4.3" fill="none" stroke="var(--green)"/><path d="M2.8 5.2 L4.4 6.7 L7.3 3.6" fill="none" stroke="var(--green)"/></svg>MAILING</li>
    <li><svg class="tick" viewBox="0 0 10 10"><circle cx="5" cy="5" r="4.3" fill="none" stroke="var(--green)"/><path d="M2.8 5.2 L4.4 6.7 L7.3 3.6" fill="none" stroke="var(--green)"/></svg>PACKAGING</li>
    <li><svg class="tick" viewBox="0 0 10 10"><circle cx="5" cy="5" r="4.3" fill="none" stroke="var(--green)"/><path d="M2.8 5.2 L4.4 6.7 L7.3 3.6" fill="none" stroke="var(--green)"/></svg>SALES</li>
  </ul>
  <ul class="industries industries--b tick-list">
    <li><svg class="tick" viewBox="0 0 10 10"><circle cx="5" cy="5" r="4.3" fill="none" stroke="var(--green)"/><path d="M2.8 5.2 L4.4 6.7 L7.3 3.6" fill="none" stroke="var(--green)"/></svg>AUTOMOTIVE</li>
    <li><svg class="tick" viewBox="0 0 10 10"><circle cx="5" cy="5" r="4.3" fill="none" stroke="var(--green)"/><path d="M2.8 5.2 L4.4 6.7 L7.3 3.6" fill="none" stroke="var(--green)"/></svg>ASSEMBLY</li>
    <li><svg class="tick" viewBox="0 0 10 10"><circle cx="5" cy="5" r="4.3" fill="none" stroke="var(--green)"/><path d="M2.8 5.2 L4.4 6.7 L7.3 3.6" fill="none" stroke="var(--green)"/></svg>CUSTOMER SVC.</li>
    <li><svg class="tick" viewBox="0 0 10 10"><circle cx="5" cy="5" r="4.3" fill="none" stroke="var(--green)"/><path d="M2.8 5.2 L4.4 6.7 L7.3 3.6" fill="none" stroke="var(--green)"/></svg>HOSPITALITY</li>
    <li><svg class="tick" viewBox="0 0 10 10"><circle cx="5" cy="5" r="4.3" fill="none" stroke="var(--green)"/><path d="M2.8 5.2 L4.4 6.7 L7.3 3.6" fill="none" stroke="var(--green)"/></svg>FULFILLMENT</li>
    <li><svg class="tick" viewBox="0 0 10 10"><circle cx="5" cy="5" r="4.3" fill="none" stroke="var(--green)"/><path d="M2.8 5.2 L4.4 6.7 L7.3 3.6" fill="none" stroke="var(--green)"/></svg>MANUFACTURING</li>
    <li><svg class="tick" viewBox="0 0 10 10"><circle cx="5" cy="5" r="4.3" fill="none" stroke="var(--green)"/><path d="M2.8 5.2 L4.4 6.7 L7.3 3.6" fill="none" stroke="var(--green)"/></svg>PRINTING</li>
    <li><svg class="tick" viewBox="0 0 10 10"><circle cx="5" cy="5" r="4.3" fill="none" stroke="var(--green)"/><path d="M2.8 5.2 L4.4 6.7 L7.3 3.6" fill="none" stroke="var(--green)"/></svg>WELDING</li>
  </ul>
</section>

</body>
</html>
```